Clean energy startup needs brochure & datasheet

• We are a solar energy start-up providing solar hybrid solutions for off-grid power demand. We need a brochure for our flagship product: our modular, transportable solar power generator, which can be installed in addition to diesel generators or batteries.
• Please visit our website www.voltarine.com to get a better feel for what we do.
• The goal of this brochure is to explain how our solar generator works and that Voltarine provides 2 different types of systems (solar-diesel and solar-battery), according to the customer needs.
• Size of the brochure (each page) is A4
• It will mostly be sent by email, so all pages should look good even if the viewer can see only one page (no graphics spanning several pages)
• A key challenge is the very high density of information on our pages - the color scheme should help in separating the main points and highlight the main conclusions
Updates

Project Deadline Extended
Reason: We still have multiple designs under consideration and need more time to work out the details.

Project Deadline Extended
Reason: We are getting close ! We were quite late in giving feedback last week, sorry for that. Thus, we give you some more time to finalise your job. Good luck !

Target Market(s)

Potential customers, meaning people all the way from diesel technicians to executives working in various sectors (prime markets are mining, light industry, construction, utilities, real estate,…)

Industry/Entity Type

Solar Energy

Font styles to use
Serif
Sans Serif

Requirements
Must have
• • Design a clean, easy to read, 4 page-brochure (A4 format bifold) with general explanations of the systems (see attached file 6 for the content and some layout ideas)
• Design one inlay datasheet (A4 double sided) with some specific technical specs of the various equipment sizes, to added in the brochure (see attached file 6 for the content and some layout ideas)
• Use Voltarine logo and derive a color scheme from our logos (there are several versions in orange, gray and white, allowing a choice of potential color schemes)
• Designers should propose multiple backgrounds for our solar generator pictures (the files with solar racking with a currently transparent background), e.g. Middle East (Desert) / Africa (Savannah) / Afghanistan (Mountains)
• Ability to edit raw files in Adobe Illustrator / Photoshop (please check with us if you want to use another program)

Nice to have
• • Provision to change pictures later (as we get real pictures from our demo plants)
Should not have
• • Any images or allusions to wind power, biomass, or other forms of renewable energy that are not solar
• Any images or allusions to green European looking landscapes (lawns, green trees, etc.) - this is a product for the Middle East & Africa!
• Any images or allusions to people in suits - this is an industrial product

```html
<!DOCTYPE html>
<html lang="en">
<head>
<meta charset="utf-8">
<title>Voltarine – Solar Generator Datasheet</title>
<link href="https://fonts.googleapis.com/css2?family=Source+Sans+3:wght@400;600;700&display=swap" rel="stylesheet">
<style>
:root{
  --orange:#f7a21b;
  --orange-deep:#f08a1c;
  --grey-text:#3c3c3c;
  --rule:#b9b9b9;
  --zero:#d6edf2;
  --h1:#fcc900;
  --h2:#f9ab1d;
  --h3:#f58a21;
  --h4:#ef6a24;
  --h5:#e94e25;
  --h6:#e23422;
  --white:#ffffff;
}
*{box-sizing:border-box;margin:0;padding:0}
html,body{width:848px;height:1200px;overflow:hidden}
body{
  font-family:"Source Sans 3",Arial,sans-serif;
  color:var(--grey-text);
  background:linear-gradient(135deg,#fcc77a 0%,#f9ad45 55%,#f7a030 100%);
  position:relative;
}
sub,sup{line-height:0;font-size:70%}
.sheet{position:absolute;left:30px;top:0;width:790px;height:1176px;background:var(--white);padding:0 40px}
.section-title{color:var(--orange-deep);font-weight:700;font-size:21px;line-height:24px}
.config-title{margin-top:92px}

.config{margin-top:9px;width:713px;border-collapse:collapse;table-layout:fixed;font-size:11.5px}
.config th{background:var(--orange);color:var(--white);font-weight:700;font-size:12px;height:46px;line-height:1.1;text-transform:uppercase;text-align:center}
.config td{border-bottom:1px solid var(--rule);height:29px;text-align:center;padding:0 6px;white-space:nowrap;line-height:1.2}
.config td+td{border-left:1px solid var(--rule)}
.config .label{text-align:left;color:var(--orange-deep);font-weight:600}
.config .group+.label{border-left:none}
.config .sub{padding-left:10px;font-size:11px}
.config .group{background:var(--orange);color:var(--white);font-weight:700;font-size:10.5px;padding:0;border-bottom:1px solid var(--white)}
.group span{display:inline-block;writing-mode:vertical-rl;transform:rotate(180deg);line-height:1;text-align:center}
.config .visual-row td{height:70px}
.panel-visual{display:block;margin:0 auto;width:146px;height:56px;background:linear-gradient(160deg,#2a3f6e 0%,#5a6f97 55%,#c9cfd8 100%);border-radius:2px}
.config .tall td{height:38px}

.notes{margin-top:8px;list-style:none;font-size:11px;line-height:18px}
.notes li{padding-left:14px;position:relative}
.notes li::before{content:"";position:absolute;left:0;top:5px;border-left:6px solid var(--orange);border-top:4px solid transparent;border-bottom:4px solid transparent}

.gen-title{margin-top:22px}
.gen-sub{margin-top:2px;font-size:14px;line-height:18px;font-weight:700;color:#4a4a4a}
.unit{margin-top:6px;font-size:9.5px;line-height:14px;font-style:italic}

.heat{margin-top:8px;border-collapse:separate;border-spacing:1px;font-size:9.6px;table-layout:fixed}
.heat td,.heat th{width:24.5px;height:24px;text-align:center;font-weight:400;background:var(--zero);white-space:nowrap}
.heat thead th{background:var(--orange);color:var(--white);height:21px;font-size:7.5px;font-weight:600}
.heat thead .hour{writing-mode:vertical-rl;transform:rotate(180deg)}
.heat .corner{width:48px}
.heat .month{width:48px;background:none;color:var(--orange-deep);font-size:10.5px}
.heat .total{width:50px;background:none;color:var(--orange-deep);font-size:10.5px;text-align:right}
.heat thead .total-head{background:none;color:var(--orange-deep);font-size:8px;line-height:1.15;text-align:right;vertical-align:top}
.heat .year-label{background:none;color:var(--orange-deep);font-size:9px;text-align:right;font-weight:600}
.heat .a{background:var(--h1)}.heat .b{background:var(--h2)}.heat .c{background:var(--h3)}
.heat .d{background:var(--h4)}.heat .e{background:var(--h5)}.heat .f{background:var(--h6)}

.footer{position:absolute;left:40px;right:40px;top:1108px;height:40px;display:flex;align-items:center}
.brand{display:flex;align-items:center;gap:8px;font-size:21px;font-weight:700;color:#4a4a4a;width:160px}
.brand i{display:block;width:16px;height:16px;border-radius:50%;background:var(--orange)}
.contact{font-size:13.5px;font-weight:600;color:#4a4a4a;margin-left:40px}
.contact b{margin-left:12px;font-weight:600}
.web{margin-left:auto;font-size:13.5px;font-weight:600;color:var(--orange-deep)}
</style>
</head>
<body>
<div class="sheet">
  <h1 class="section-title config-title">Solar Generator Configuration Options</h1>
  <table class="config">
    <colgroup><col style="width:54px"><col style="width:176px"><col style="width:163px"><col style="width:158px"><col style="width:162px"></colgroup>
    <thead>
      <tr><th colspan="2"></th><th>Single Block</th><th>Full 20'<br>Container</th><th>Full 40'<br>Container</th></tr>
    </thead>
    <tbody>
      <tr class="visual-row"><td colspan="2"></td>
        <td><span class="panel-visual" role="img" aria-label="Single solar racking block with panels"></span></td>
        <td><span class="panel-visual" role="img" aria-label="Three solar racking blocks from a 20 foot container"></span></td>
        <td><span class="panel-visual" role="img" aria-label="Seven solar racking blocks from a 40 foot container"></span></td></tr>
      <tr><td class="label" colspan="2">Solar generator capacity (kWp<sub>DC</sub>)<sup>1)</sup></td><td>24</td><td>72</td><td>168</td></tr>
      <tr><td class="label" colspan="2">Peak output (kW<sub>AC</sub> / kVA)</td><td>20</td><td>60</td><td>140</td></tr>
      <tr><td class="group" rowspan="4"><span>Avgerage<br>energy<br>generation<sup>2)</sup></span></td><td class="label sub">Daily min. (kWh<sub>AC</sub> / day)</td><td>96</td><td>288</td><td>672</td></tr>
      <tr><td class="label sub">Daily max. (kWh<sub>AC</sub> / day)</td><td>120</td><td>360</td><td>840</td></tr>
      <tr><td class="label sub">Annually min. (kWh<sub>AC</sub> / year)</td><td>35'040</td><td>105'120</td><td>245'600</td></tr>
      <tr><td class="label sub">Annually max. (kWh<sub>AC</sub> / year)</td><td>43'800</td><td>131'400</td><td>306'600</td></tr>
      <tr><td class="label" colspan="2">Module area (m2)</td><td>158</td><td>475</td><td>1'109</td></tr>
      <tr class="tall"><td class="label" colspan="2">Layout options<sup>3)</sup></td><td>50m x 4m (single row)<br>25m x 12m (double row)</td><td>75m x 12 m (double row)<br>50m x 20m (triple row)</td><td>75m x 36m (5 rows)<br>50m x 52m (7 rows)</td></tr>
      <tr class="tall"><td class="label" colspan="2">Recommended minimum<br>diesel generator capacity (kVA)</td><td>~50</td><td>~100</td><td>~250</td></tr>
      <tr><td class="label" colspan="2">Battery capacity</td><td colspan="3">Up to 24h (on request)</td></tr>
    </tbody>
  </table>
  <ul class="notes">
    <li>Other capacities are available in multiples of 24 kWp.</li>
    <li>Typical range up to 30° latitude. Actual output depends on the exact location.</li>
    <li>Other layouts available on request.</li>
  </ul>

  <h2 class="section-title gen-title">Typical Energy Generation During the Day</h2>
  <p class="gen-sub">Standard 24 kWp Solar Generator Block</p>
  <p class="unit">SOLAR kWh</p>
  <table class="heat">
    <thead>
      <tr><th class="corner">TIME</th>
        <th class="hour" rowspan="2">00:00</th><th class="hour" rowspan="2">01:00</th><th class="hour" rowspan="2">02:00</th><th class="hour" rowspan="2">03:00</th><th class="hour" rowspan="2">04:00</th><th class="hour" rowspan="2">05:00</th><th class="hour" rowspan="2">06:00</th><th class="hour" rowspan="2">07:00</th><th class="hour" rowspan="2">08:00</th><th class="hour" rowspan="2">09:00</th><th class="hour" rowspan="2">10:00</th><th class="hour" rowspan="2">11:00</th><th class="hour" rowspan="2">12:00</th><th class="hour" rowspan="2">13:00</th><th class="hour" rowspan="2">14:00</th><th class="hour" rowspan="2">15:00</th><th class="hour" rowspan="2">16:00</th><th class="hour" rowspan="2">17:00</th><th class="hour" rowspan="2">18:00</th><th class="hour" rowspan="2">19:00</th><th class="hour" rowspan="2">20:00</th><th class="hour" rowspan="2">21:00</th><th class="hour" rowspan="2">22:00</th><th class="hour" rowspan="2">23:00</th>
        <th class="total-head" rowspan="2">MONTHLY<br>TOTAL</th></tr>
      <tr><th class="corner">MONTH</th></tr>
    </thead>
    <tbody>
      <tr><th class="month">JAN</th><td>0.0</td><td>0.0</td><td>0.0</td><td>0.0</td><td>0.0</td><td>0.0</td><td>0.0</td><td>0.0</td><td class="a">0.9</td><td class="b">4.1</td><td class="c">8.0</td><td class="d">11.7</td><td class="d">13.8</td><td class="e">15.5</td><td class="e">14.4</td><td class="d">11.7</td><td class="c">8.7</td><td class="b">4.6</td><td class="a">1.2</td><td>0.0</td><td>0.0</td><td>0.0</td><td>0.0</td><td>0.0</td><td class="total">2'931</td></tr>
      <tr><th class="month">FEB</th><td>0.0</td><td>0.0</td><td>0.0</td><td>0.0</td><td>0.0</td><td>0.0</td><td>0.0</td><td>0.0</td><td class="a">1.7</td><td class="b">6.2</td><td class="c">10.6</td><td class="e">14.1</td><td class="f">16.3</td><td class="f">17.2</td><td class="f">16.2</td><td class="d">13.9</td><td class="c">10.4</td><td class="b">5.9</td><td class="a">1.7</td><td>0.0</td><td>0.0</td><td>0.0</td><td>0.0</td><td>0.0</td><td class="total">3'196</td></tr>
      <tr><th class="month">MAR</th><td>0.0</td><td>0.0</td><td>0.0</td><td>0.0</td><td>0.0</td><td>0.0</td><td>0.0</td><td>0.0</td><td class="a">2.9</td><td class="c">7.4</td><td class="d">11.3</td><td class="e">14.3</td><td class="f">16.2</td><td class="f">16.9</td><td class="e">15.6</td><td class="d">13.8</td><td class="c">10.8</td><td class="b">6.6</td><td class="a">2.3</td><td>0.0</td><td>0.0</td><td>0.0</td><td>0.0</td><td>0.0</td><td class="total">3'665</td></tr>
      <tr><th class="month">APR</th><td>0.0</td><td>0.0</td><td>0.0</td><td>0.0</td><td>0.0</td><td>0.0</td><td>0.0</td><td class="a">1.3</td><td class="b">5.1</td><td class="c">9.1</td><td class="d">12.8</td><td class="f">16.2</td><td class="f">17.6</td><td class="f">18.3</td><td class="f">17.7</td><td class="e">15.8</td><td class="d">12.2</td><td class="c">7.9</td><td class="b">3.4</td><td class="a">0.3</td><td>0.0</td><td>0.0</td><td>0.0</td><td>0.0</td><td class="total">4'130</td></tr>
      <tr><th class="month">MAY</th><td>0.0</td><td>0.0</td><td>0.0</td><td>0.0</td><td>0.0</td><td>0.0</td><td class="a">2.3</td><td class="a">2.3</td><td class="b">6.3</td><td class="c">10.4</td><td class="d">13.6</td><td class="e">15.9</td><td class="f">17.4</td><td class="f">17.9</td><td class="f">17.0</td><td class="e">15.2</td><td class="d">12.3</td><td class="c">8.4</td><td class="b">4.1</td><td class="a">0.7</td><td>0.0</td><td>0.0</td><td>0.0</td><td>0.0</td><td class="total">4'390</td></tr>
      <tr><th class="month">JUN</th><td>0.0</td><td>0.0</td><td>0.0</td><td>0.0</td><td>0.0</td><td>0.0</td><td class="a">0.2</td><td class="a">2.4</td><td class="b">6.0</td><td class="c">9.6</td><td class="d">12.3</td><td class="e">14.4</td><td class="e">15.8</td><td class="f">16.3</td><td class="e">15.8</td><td class="e">14.1</td><td class="d">11.5</td><td class="c">8.0</td><td class="b">4.3</td><td class="a">1.1</td><td>0.0</td><td>0.0</td><td>0.0</td><td>0.0</td><td class="total">3'958</td></tr>
      <tr><th class="month">JUL</th><td>0.0</td><td>0.0</td><td>0.0</td><td>0.0</td><td>0.0</td><td>0.0</td><td>0.0</td><td class="a">1.6</td><td class="b">4.8</td><td class="c">8.4</td><td class="d">11.6</td><td class="e">14.5</td><td class="f">16.0</td><td class="f">16.4</td><td class="f">16.0</td><td class="e">14.2</td><td class="d">11.3</td><td class="c">7.7</td><td class="b">4.0</td><td class="a">1.0</td><td>0.0</td><td>0.0</td><td>0.0</td><td>0.0</td><td class="total">3'953</td></tr>
      <tr><th class="month">AUG</th><td>0.0</td><td>0.0</td><td>0.0</td><td>0.0</td><td>0.0</td><td>0.0</td><td>0.0</td><td class="a">1.2</td><td class="b">4.7</td><td class="c">8.7</td><td class="d">12.2</td><td class="e">14.8</td><td class="f">16.5</td><td class="f">17.0</td><td class="f">16.2</td><td class="e">14.1</td><td class="d">11.3</td><td class="c">7.5</td><td class="b">3.4</td><td class="a">0.6</td><td>0.0</td><td>0.0</td><td>0.0</td><td>0.0</td><td class="total">3'977</td></tr>
      <tr><th class="month">SEP</th><td>0.0</td><td>0.0</td><td>0.0</td><td>0.0</td><td>0.0</td><td>0.0</td><td>0.0</td><td class="a">0.9</td><td class="b">4.6</td><td class="c">9.0</td><td class="d">12.7</td><td class="e">15.4</td><td class="f">16.9</td><td class="f">17.2</td><td class="f">16.3</td><td class="e">14.1</td><td class="c">10.9</td><td class="b">6.7</td><td class="a">2.2</td><td>0.0</td><td>0.0</td><td>0.0</td><td>0.0</td><td>0.0</td><td class="total">3'808</td></tr>
      <tr><th class="month">OCT</th><td>0.0</td><td>0.0</td><td>0.0</td><td>0.0</td><td>0.0</td><td>0.0</td><td>0.0</td><td class="a">0.8</td><td class="b">3.9</td><td class="c">8.4</td><td class="d">12.1</td><td class="e">14.9</td><td class="f">16.4</td><td class="f">16.4</td><td class="e">15.3</td><td class="d">12.8</td><td class="c">8.9</td><td class="b">4.3</td><td class="a">0.9</td><td>0.0</td><td>0.0</td><td>0.0</td><td>0.0</td><td>0.0</td><td class="total">3'455</td></tr>
      <tr><th class="month">NOV</th><td>0.0</td><td>0.0</td><td>0.0</td><td>0.0</td><td>0.0</td><td>0.0</td><td>0.0</td><td>0.0</td><td class="a">2.8</td><td class="c">7.1</td><td class="c">10.8</td><td class="d">13.5</td><td class="e">15.3</td><td class="e">15.2</td><td class="e">14.0</td><td class="d">11.7</td><td class="c">7.8</td><td class="b">3.1</td><td>0.0</td><td>0.0</td><td>0.0</td><td>0.0</td><td>0.0</td><td>0.0</td><td class="total">3'042</td></tr>
      <tr><th class="month">DEC</th><td>0.0</td><td>0.0</td><td>0.0</td><td>0.0</td><td>0.0</td><td>0.0</td><td>0.0</td><td>0.0</td><td class="a">1.6</td><td class="b">5.1</td><td class="c">8.9</td><td class="d">11.4</td><td class="d">12.6</td><td class="d">12.7</td><td class="d">12.0</td><td class="c">10.1</td><td class="b">6.6</td><td class="a">2.5</td><td>0.0</td><td>0.0</td><td>0.0</td><td>0.0</td><td>0.0</td><td>0.0</td><td class="total">2'591</td></tr>
      <tr><th class="month"></th><td colspan="24" class="year-label">YEAR TOTAL</td><td class="total">43'096</td></tr>
    </tbody>
  </table>

  <footer class="footer">
    <div class="brand"><i></i>Voltarine</div>
    <p class="contact">For more information contact us.<b>+971.4.555.0182</b></p>
    <p class="web">www.voltarine.com</p>
  </footer>
</div>
</body>
</html>
```